Restaurant needs a vertical banner for fried catfish

Our restaurant is looking for an eye-catching 78.75in. x 36in. vertical physical banner ad for our fried catfish. Photos for the fried catfish will be provided as a reference but we will also accept anything similar to the photo. We will be using the following as our receptacle: https://www.plankoria.example/banner-stand/retractable-banner-stands/
The design must incorporate the following flavor texts:
Fried Catfish
Always Fresh!
Made from Scratch
Hand-cut Fillets
The Best Catfish in Texas
Served with fries, hush puppies, and a 32oz fountain drink
Also available by the pound!
The final design should be creative, professional, and eye-catching for customers.
Updates
Colors
Designer to choose colors to be used in the design.
Requirements
Must have
- We are open to any and all design elements, albeit the 'flavor texts' should not overpower, but complement the fried catfish photo. 'Fried Catfish' can be used in lieu of a main title/logo.
Nice to have
- Transparent or textured backgrounds that can encompass any or all part of the banner such as a cutting board, shadows, abstract, etc to show depth are a plus.
- Use of vectors or objects such as ribbons or shapes to encapsulate the 'flavor texts' are also encouraged.

```html
<!DOCTYPE html>
<html lang="en">
<head>
<meta charset="utf-8">
<title>Fried Catfish Vertical Banner</title>
<link rel="stylesheet" href="https://fonts.googleapis.com/css2?family=Exo+2:wght@700&family=Hind:wght@600&family=Montserrat:wght@300;400;800;900&display=swap">
<style>
  :root {
    --stage: #e4e4e4;
    --ink: #141414;
    --ink-soft: #262626;
    --gold: #f3b70c;
    --white: #ffffff;
    --plate: #f4f2ec;
    --crust: #b8741f;
    --crust-dark: #8a521a;
    --fries: #f0c75a;
  }
  html, body {
    margin: 0;
    padding: 0;
    width: 1200px;
    height: 3448px;
    overflow: hidden;
    background: var(--stage);
  }
  .banner {
    position: absolute;
    left: 80px;
    top: 584px;
    width: 1040px;
    height: 2280px;
    background:
      radial-gradient(ellipse at 30% 20%, var(--ink-soft) 0%, transparent 60%),
      radial-gradient(ellipse at 75% 70%, #202020 0%, transparent 55%),
      var(--ink);
    box-shadow: 0 12px 30px rgba(0,0,0,0.35);
    overflow: hidden;
  }
  .title {
    position: absolute;
    left: 0;
    width: 100%;
    text-align: center;
    margin: 0;
    font-family: "Exo 2", sans-serif;
    font-weight: 700;
    line-height: 1;
  }
  .title--fried { top: 104px; font-size: 204px; color: var(--white); letter-spacing: 4px; }
  .title--catfish { top: 286px; font-size: 204px; color: var(--gold); letter-spacing: 4px; }
  .dish-photo {
    position: absolute;
    left: 80px;
    top: 555px;
    width: 880px;
    height: 490px;
    border-radius: 46% / 50%;
    background:
      linear-gradient(115deg,
        var(--fries) 0%,
        #e6a84a 22%,
        var(--crust) 40%,
        var(--crust-dark) 52%,
        var(--crust) 64%,
        #d9a766 76%,
        var(--plate) 90%,
        #e8e4da 100%);
    box-shadow: 0 0 0 14px var(--plate), 0 18px 40px rgba(0,0,0,0.6);
  }
  .features {
    position: absolute;
    left: 100px;
    top: 1155px;
    width: 880px;
    margin: 0;
    padding: 0;
    list-style: none;
    display: grid;
    grid-template-columns: 452px 1fr;
    row-gap: 38px;
    font-family: "Hind", sans-serif;
    font-weight: 600;
    font-size: 52px;
    line-height: 0.98;
    color: var(--white);
  }
  .feature { display: flex; align-items: flex-start; gap: 18px; }
  .feature svg { flex: none; width: 40px; height: 40px; margin-top: 4px; }
  .claim {
    position: absolute;
    left: 0;
    width: 100%;
    text-align: center;
    font-family: "Montserrat", sans-serif;
    margin: 0;
    line-height: 1;
  }
  .claim--lead { top: 1460px; font-size: 66px; font-weight: 800; color: var(--white); }
  .claim--main { top: 1530px; font-size: 78px; font-weight: 900; color: var(--gold); }
  .claim--pound { top: 1632px; font-size: 46px; font-weight: 400; color: var(--white); letter-spacing: 3px; }
  .divider { position: absolute; left: 115px; top: 1712px; width: 810px; height: 20px; }
  .serving {
    position: absolute;
    left: 0;
    top: 1802px;
    width: 100%;
    text-align: center;
    font-family: "Montserrat", sans-serif;
    font-weight: 300;
    font-size: 38px;
    line-height: 1.3;
    color: var(--white);
    margin: 0;
  }
  .phone-band {
    position: absolute;
    left: 0;
    top: 1962px;
    width: 100%;
    height: 176px;
    background: var(--gold);
    display: flex;
    align-items: center;
    justify-content: center;
    gap: 28px;
  }
  .phone-band svg { width: 86px; height: 86px; }
  .phone-number {
    font-family: "Montserrat", sans-serif;
    font-weight: 800;
    font-size: 110px;
    color: var(--ink);
    letter-spacing: 1px;
  }
  .web-address {
    position: absolute;
    left: 0;
    top: 2188px;
    width: 100%;
    text-align: center;
    font-family: "Montserrat", sans-serif;
    font-weight: 800;
    font-size: 36px;
    letter-spacing: 11px;
    color: var(--white);
  }
</style>
</head>
<body>
  <main class="banner">
    <h1 class="title title--fried">FRIED</h1>
    <h1 class="title title--catfish">CATFISH</h1>

    <div class="dish-photo" role="img" aria-label="Photo of golden fried catfish fillets with french fries, two hush puppies and a tartar sauce cup on a white plate"></div>

    <ul class="features">
      <li class="feature">
        <svg viewBox="0 0 40 40"><circle cx="20" cy="20" r="17" fill="none" stroke="var(--gold)" stroke-width="3"/><path d="M12 20l6 6 11-12" fill="none" stroke="var(--gold)" stroke-width="3.5" stroke-linecap="round" stroke-linejoin="round"/></svg>
        <span>Fried Catfish</span>
      </li>
      <li class="feature">
        <svg viewBox="0 0 40 40"><circle cx="20" cy="20" r="17" fill="none" stroke="var(--gold)" stroke-width="3"/><path d="M12 20l6 6 11-12" fill="none" stroke="var(--gold)" stroke-width="3.5" stroke-linecap="round" stroke-linejoin="round"/></svg>
        <span>Always Fresh!</span>
      </li>
      <li class="feature">
        <svg viewBox="0 0 40 40"><circle cx="20" cy="20" r="17" fill="none" stroke="var(--gold)" stroke-width="3"/><path d="M12 20l6 6 11-12" fill="none" stroke="var(--gold)" stroke-width="3.5" stroke-linecap="round" stroke-linejoin="round"/></svg>
        <span>Made from<br>Scratch</span>
      </li>
      <li class="feature">
        <svg viewBox="0 0 40 40"><circle cx="20" cy="20" r="17" fill="none" stroke="var(--gold)" stroke-width="3"/><path d="M12 20l6 6 11-12" fill="none" stroke="var(--gold)" stroke-width="3.5" stroke-linecap="round" stroke-linejoin="round"/></svg>
        <span>Hand-cut<br>Fillets</span>
      </li>
    </ul>

    <p class="claim claim--lead">THE BEST</p>
    <p class="claim claim--main">CATFISH IN TEXAS</p>
    <p class="claim claim--pound">ALSO AVAILABLE BY THE POUND!</p>

    <svg class="divider" viewBox="0 0 810 20">
      <line x1="0" y1="10" x2="810" y2="10" stroke="var(--gold)" stroke-width="2"/>
      <rect x="365" y="3" width="80" height="14" fill="var(--gold)"/>
    </svg>

    <p class="serving">Served with fries, hush puppies and<br>a 32oz fountain drink</p>

    <div class="phone-band">
      <svg viewBox="0 0 86 86">
        <circle cx="43" cy="43" r="40" fill="var(--ink)"/>
        <path d="M31 22c3 0 5 6 6 9 1 2-3 5-3 6 2 6 7 11 13 14 1 0 4-4 6-3 3 1 9 3 9 6 0 4-4 9-9 9-16-2-29-15-31-31 0-5 5-10 9-10z" fill="var(--gold)"/>
      </svg>
      <span class="phone-number">5550148273</span>
    </div>

    <div class="web-address">www.catfishplate.example</div>
  </main>
</body>
</html>
```